PRK website

Im a Specialty contractor that specializes in fireproofing. Epoxy flooring and terrazo along with poured floors and polished concrete.

We also do fire caulking.

Im the largest specialty flooring healthcare contractor in the south east.

Otto

Contractor

```html
<!DOCTYPE html>
<html lang="en">
<head>
<meta charset="utf-8">
<title>PRK – Fireproofing &amp; Specialty Flooring</title>
<link rel="stylesheet" href="https://fonts.googleapis.com/css2?family=Roboto:ital,wght@0,300;0,400;0,500;0,700;0,900;1,300;1,700&family=Roboto+Condensed:wght@700&display=swap">
<style>
:root{
  --bg-top:#2a3843;
  --bg-bottom:#1b242b;
  --panel-dark:#232f38;
  --footer:#1a2127;
  --white:#ffffff;
  --ink:#1c1c1c;
  --body:#333333;
  --muted:#8e969b;
  --grey-box:#d1d3d5;
  --accent:#d5561f;
  --purple:#8a3d8f;
  --rule:#4a5760;
  --terrazzo-a:#f1efec;
  --terrazzo-b:#e3dfda;
  --tile-a:#c9563a;
  --tile-b:#9e3b25;
}
*{box-sizing:border-box;margin:0;padding:0}
html,body{width:871px;height:1200px;overflow:hidden}
body{
  position:relative;
  font-family:"Roboto",Arial,sans-serif;
  background:linear-gradient(160deg,var(--bg-top),var(--bg-bottom));
  color:var(--white);
}
.abs{position:absolute}

/* header */
.site-title{left:83px;top:46px;font-size:45px;font-weight:900;letter-spacing:.5px}
.contact-head{right:92px;top:50px;text-align:right}
.contact-head .phone{font-size:25px;font-weight:700;display:flex;align-items:center;gap:8px;justify-content:flex-end}
.contact-head .address{font-size:11.5px;font-weight:700;margin-top:-2px}
.header-rule{left:34px;top:118px;width:799px;height:1px;background:linear-gradient(90deg,var(--rule),var(--rule) 85%,transparent)}
.main-nav{left:84px;top:133px;display:flex;gap:34px;font-size:15.5px;font-weight:500;letter-spacing:.6px}
.main-nav a{color:var(--white);text-decoration:none}

/* hero */
.hero-frame{left:34px;top:174px;width:803px;height:273px;border-radius:26px;
  background:linear-gradient(135deg,var(--terrazzo-a),var(--terrazzo-b))}
.hero-panel{left:43px;top:183px;width:777px;height:256px;border-radius:18px;
  background:linear-gradient(160deg,#2b3944,var(--panel-dark))}
.hero-image{left:436px;top:191px;width:384px;height:239px;
  background:radial-gradient(circle at 40% 40%,#f6f5f3,#e1ddd8)}
.hero-kicker{left:85px;top:278px;font-size:22px;font-weight:300;font-style:italic;letter-spacing:.3px}
.hero-title{left:83px;top:298px;font-size:44px;font-weight:700;letter-spacing:-.5px}
.hero-title .dim{color:var(--muted)}

/* content */
.content-card{left:34px;top:473px;width:803px;height:412px;border-radius:24px;background:var(--white);color:var(--body)}
.section-title{font-family:"Roboto Condensed",Arial,sans-serif;font-weight:700;font-size:18px;color:var(--ink)}
.intro{left:51px;top:40px;width:320px}
.intro .lead{font-size:12.5px;font-weight:700;color:var(--ink);line-height:17px;margin-top:16px}
.intro .text{font-size:12.5px;line-height:17px;margin-top:16px}
.feature-list{list-style:none;margin-top:17px;padding-left:12px}
.feature-list li{font-size:13px;font-weight:700;color:var(--accent);line-height:22.2px;position:relative;padding-left:17px}
.feature-list li::before{content:"";position:absolute;left:0;top:7px;width:9px;height:9px;border-radius:50%;
  background:radial-gradient(circle at 35% 35%,#888,#333)}
.news{left:402px;top:17px;width:384px;height:378px;border-radius:6px;background:var(--grey-box);padding:23px 0 0 50px}
.news-item{display:flex;gap:14px;margin-top:23px}
.news-item + .news-item{margin-top:24px}
.thumb{width:77px;height:77px;border-radius:10px;border:3px solid #2a2a2a;flex:none;
  background:radial-gradient(circle at 40% 40%,var(--tile-a),var(--tile-b))}
.news-item h3{font-size:15.5px;font-weight:400;color:var(--ink)}
.news-item .sub{font-size:11.5px;font-weight:700;font-style:italic;color:var(--purple);margin-top:1px}
.news-item p{font-size:11px;line-height:13px;margin-top:3px;color:#444}
.news-item .more{font-size:11.5px;font-weight:700;color:var(--ink);text-decoration:none;display:inline-flex;gap:5px;align-items:center;margin-top:4px}

/* footer */
.site-footer{left:34px;top:910px;width:803px;height:274px;border-radius:24px;background:linear-gradient(160deg,#222b32,var(--footer))}
.footer-title{font-size:15.5px;font-weight:700}
.address-block{top:27px;width:170px}
.address-block p{font-size:12px;line-height:20.5px;margin-top:8px}
.badges{display:flex;gap:8px;margin-top:11px}
.badge{width:55px;height:34px;border-radius:3px;background:#e9ecef;color:#1c3a72;font-size:10px;font-weight:700;display:flex;align-items:center;justify-content:center}
.badge.dark{background:#1f4f8f;color:var(--white)}
.social{display:flex;gap:10px;margin-top:11px}
.social span{width:32px;height:32px;border-radius:6px;background:#e8edf1;color:#2b4a63;font-size:8px;font-weight:700;display:flex;align-items:center;justify-content:center}
.contact-form{left:581px;top:27px}
.contact-form .field{display:block;width:136px;height:19px;background:var(--white);color:#aaa;font-size:11px;padding:2px 5px;margin-top:8px}
.contact-form .field.first{margin-top:17px}
.contact-form .message{width:188px;height:103px;margin-top:10px;background:linear-gradient(#fff,#f1f1f1)}
.contact-form .send{width:61px;height:24px;margin-top:8px;background:linear-gradient(#fafafa,#dcdcdc);color:var(--ink);font-size:12.5px;font-weight:700;display:flex;align-items:center;justify-content:center}
</style>
</head>
<body>

<header>
  <div class="abs site-title">FIREPROOFING</div>
  <div class="abs contact-head">
    <div class="phone">
      <svg width="21" height="21" viewBox="0 0 24 24" aria-hidden="true"><path fill="#fff" d="M6.6 10.8c1.4 2.8 3.8 5.1 6.6 6.6l2.2-2.2c.3-.3.7-.4 1-.2 1.1.4 2.3.6 3.6.6.6 0 1 .4 1 1V20c0 .6-.4 1-1 1C10.6 21 3 13.4 3 4c0-.6.4-1 1-1h3.5c.6 0 1 .4 1 1 0 1.3.2 2.5.6 3.6.1.3 0 .7-.2 1z" transform="rotate(90 12 12)"/></svg>
      (200) 555-0147
    </div>
    <div class="address">3577 Street, City, ZIP</div>
  </div>
  <div class="abs header-rule"></div>
  <nav class="abs main-nav">
    <a href="#">home</a><a href="#">fireprofing</a><a href="#">epoxy</a><a href="#">terrazo</a><a href="#">pored floors</a><a href="#">polished concrete</a><a href="#">contact</a>
  </nav>
</header>

<section class="hero">
  <div class="abs hero-frame"></div>
  <div class="abs hero-panel"></div>
  <div class="abs hero-image" role="img" aria-label="Close-up of a polished terrazzo floor with coloured stone chips"></div>
  <div class="abs hero-kicker">LEGERE CUM FORTE</div>
  <div class="abs hero-title"><span class="dim">OMNES</span> VERO</div>
</section>

<main class="abs content-card">
  <div class="abs intro">
    <h2 class="section-title">Per esse magna exerci</h2>
    <p class="lead">In bonorum laboramus pri, in congue animal dissentiet sed. Eu cum harum mundi oportere.</p>
    <p class="text">Ne audiam ocurreret constituam eam, ea sumo referrentur eum, ea sit nostro nostrum. Pri vidit percipit cotidieque ea, per omittam necessitatibus no, id per audire aliquando. Ei modo minimum erroribus quo, eos ei erat laudem omittam. Solum gloriatur ei usu. Sonet</p>
    <ul class="feature-list">
      <li>Quot illud cum ut, ut liber iusto expetendis</li>
      <li>Quot illud cum ut, ut liber iusto expetendis</li>
      <li>Quot illud cum ut, ut liber iusto expetendis</li>
      <li>Quot illud cum ut, ut liber iusto expetendis</li>
      <li>Quot illud cum ut, ut liber iusto expetendis</li>
      <li>Quot illud cum ut, ut liber iusto expetendis</li>
    </ul>
  </div>

  <aside class="abs news">
    <h2 class="section-title">Per esse magna exerci</h2>
    <article class="news-item">
      <div class="thumb" role="img" aria-label="Red epoxy floor sample"></div>
      <div><h3>Ea per latine partiendo</h3><div class="sub">Ea per latine partiendo</div><p>Sanctus scaevola disputando<br>mea et. Vel vidit audiam</p><a class="more" href="#">Read more <svg width="13" height="10" viewBox="0 0 13 10" aria-hidden="true"><path d="M1 1l4 4-4 4M7 1l4 4-4 4" fill="none" stroke="#1c1c1c" stroke-width="2"/></svg></a></div>
    </article>
    <article class="news-item">
      <div class="thumb" role="img" aria-label="Red epoxy floor sample"></div>
      <div><h3>Ea per latine partiendo</h3><div class="sub">Ea per latine partiendo</div><p>Sanctus scaevola disputando<br>mea et. Vel vidit audiam</p><a class="more" href="#">Read more <svg width="13" height="10" viewBox="0 0 13 10" aria-hidden="true"><path d="M1 1l4 4-4 4M7 1l4 4-4 4" fill="none" stroke="#1c1c1c" stroke-width="2"/></svg></a></div>
    </article>
    <article class="news-item">
      <div class="thumb" role="img" aria-label="Red epoxy floor sample"></div>
      <div><h3>Ea per latine partiendo</h3><div class="sub">Ea per latine partiendo</div><p>Sanctus scaevola disputando<br>mea et. Vel vidit audiam</p><a class="more" href="#">Read more <svg width="13" height="10" viewBox="0 0 13 10" aria-hidden="true"><path d="M1 1l4 4-4 4M7 1l4 4-4 4" fill="none" stroke="#1c1c1c" stroke-width="2"/></svg></a></div>
    </article>
  </aside>
</main>

<footer class="abs site-footer">
  <div class="abs address-block" style="left:33px">
    <h3 class="footer-title">Iriure Invidunt</h3>
    <p>2121 Sample Avenue #330<br>City Name, AB 10000<br>Phone : +1 212.000.2222<br>Fax : +1 212.000.2222<br>mail@example.com</p>
  </div>
  <div class="abs address-block" style="left:214px">
    <h3 class="footer-title">Iriure Invidunt</h3>
    <p>2121 Sample Avenue #330<br>City Name, AB 10000<br>Phone : +1 212.000.2222<br>Fax : +1 212.000.2222<br>mail@example.com</p>
  </div>
  <div class="abs address-block" style="left:393px">
    <h3 class="footer-title">Iriure Invidunt</h3>
    <p>2121 Sample Avenue #330<br>City Name, AB 10000<br>Phone : +1 212.000.2222<br>Fax : +1 212.000.2222<br>mail@example.com</p>
  </div>

  <div class="abs" style="left:35px;top:184px">
    <h3 class="footer-title">We Accept</h3>
    <div class="badges">
      <span class="badge">Paycard</span>
      <span class="badge dark">Paycard E</span>
      <span class="badge">Walletly</span>
      <span class="badge dark">Debix</span>
      <span class="badge">Crest</span>
    </div>
  </div>

  <div class="abs" style="left:392px;top:184px">
    <h3 class="footer-title">Follow Us</h3>
    <div class="social">
      <span>Chirp</span><span>Searchy</span><span>Facely</span><span>Feed</span>
    </div>
  </div>

  <form class="abs contact-form">
    <h3 class="footer-title">Contact Us</h3>
    <span class="field first">Name</span>
    <span class="field">Email</span>
    <div class="message"></div>
    <div class="send">Send</div>
  </form>
</footer>

</body>
</html>
```